The Brandwell Group Billboard Design

The Brandwell Group is doing a Motorcycle Gordon campaign and we need a billboard design. The following are the requirements:

1. We need Gordon Brandwell, who is in the photo attached, to be photoshopped into a black leather three-piece suit, white hair and beard, next to a really cool old school Tarvin Rourke motorcycle, with a South Carolina scene in the background.
2. The Billboard should have the slogan "Motorcycle Wreck? We have your back!"
3. Our logo, which is attached, needs to be on the billboard
4. Our phone number needs to be on the billboard - (555) 274-6190
5. Tarvin Rourke colors

```html
<!DOCTYPE html>
<html lang="en">
<head>
<meta charset="utf-8">
<title>Brandwell Billboard</title>
<link rel="stylesheet" href="https://fonts.googleapis.com/css2?family=Montserrat:wght@800;900&display=swap">
<style>
  :root {
    --ink: #231d1a;
    --ink-deep: #14110f;
    --orange: #f18421;
    --white: #ffffff;
    --page: #f3f3f3;
    --sky-top: #3f9fd6;
    --sky-mid: #a9c4d6;
    --sunset: #f3a86c;
    --sand: #7b726c;
  }
  html, body {
    margin: 0;
    padding: 0;
    width: 937px;
    height: 1200px;
    overflow: hidden;
    background: var(--page);
  }
  .billboard {
    position: absolute;
    left: 30px;
    top: 417px;
    width: 877px;
    height: 365px;
    display: block;
    box-shadow: 0 14px 34px rgba(0, 0, 0, 0.28);
  }
  .brand-name {
    font-family: "Montserrat", sans-serif;
    font-weight: 800;
    fill: var(--orange);
  }
  .headline {
    font-family: "Montserrat", sans-serif;
    font-weight: 800;
    fill: var(--white);
  }
  .headline-big { font-weight: 900; }
  .slogan {
    font-family: "Montserrat", sans-serif;
    font-weight: 800;
    fill: var(--orange);
  }
  .phone-number {
    font-family: "Montserrat", sans-serif;
    font-weight: 800;
    fill: var(--ink-deep);
  }
</style>
</head>
<body>
  <svg class="billboard" viewBox="0 0 1334 555" xmlns="http://www.w3.org/2000/svg" aria-label="Brandwell motorcycle wreck billboard">
    <defs>
      <linearGradient id="panelShade" x1="0" y1="0" x2="1" y2="0">
        <stop offset="0" stop-color="#1c1715"/>
        <stop offset="0.7" stop-color="#2a221e"/>
        <stop offset="1" stop-color="#201a17"/>
      </linearGradient>
      <linearGradient id="sceneTones" x1="0" y1="0" x2="0" y2="1">
        <stop offset="0" stop-color="var(--sky-top)"/>
        <stop offset="0.32" stop-color="var(--sky-mid)"/>
        <stop offset="0.52" stop-color="var(--sunset)"/>
        <stop offset="0.62" stop-color="#9a8a80"/>
        <stop offset="1" stop-color="var(--sand)"/>
      </linearGradient>
    </defs>

    <rect class="message-panel" x="0" y="0" width="1334" height="555" fill="url(#panelShade)" role="img" aria-label="Faint beachfront hotel skyline behind the headline"/>

    <polygon class="phone-band" points="0,455 760,455 822,555 0,555" fill="var(--orange)"/>

    <path class="divider-accent" d="M818,-6 L700,188" stroke="var(--orange)" stroke-width="22" fill="none"/>
    <path class="divider-accent" d="M700,368 L818,561" stroke="var(--orange)" stroke-width="22" fill="none"/>

    <polygon class="photo-frame" points="828,0 1334,0 1334,555 828,555 648,278" fill="var(--white)"/>

    <polygon class="photo-area" points="848,0 1334,0 1334,555 848,555 672,278" fill="url(#sceneTones)" role="img" aria-label="Bearded rider in black leather jacket on a classic chrome motorcycle on a beach at sunset, with a Ferris wheel and pier behind"/>

    <text class="brand-name" x="85" y="150" font-size="86" textLength="470" lengthAdjust="spacingAndGlyphs">BRANDWELL</text>

    <text class="headline" x="80" y="260" font-size="74" textLength="548" lengthAdjust="spacingAndGlyphs">MOTORCYCLE</text>
    <text class="headline headline-big" x="80" y="364" font-size="122" textLength="522" lengthAdjust="spacingAndGlyphs">WRECK?</text>
    <text class="slogan" x="78" y="420" font-size="48" textLength="560" lengthAdjust="spacingAndGlyphs">WE HAVE YOUR BACK!</text>

    <g class="phone-icon" transform="translate(102,502)">
      <circle r="27" fill="var(--ink-deep)"/>
      <path d="M-12,-9 C-12,-13 -9,-15 -6,-15 L-3,-7 L-7,-4 C-5,2 0,7 5,8 L8,4 L15,7 C15,11 12,14 8,14 C-3,13 -13,3 -12,-9 Z" fill="var(--white)"/>
    </g>
    <text class="phone-number" x="148" y="532" font-size="74" textLength="560" lengthAdjust="spacingAndGlyphs">(555) 274-6190</text>
  </svg>
</body>
</html>
```